Home Page Design (+50 More Pages To Winning Designer!)

We have a 50+ page website, but we're starting with the home page. The winning designer will get all 50+ pages to design as a 2nd project, so make sure you do your best!

SoarVane is in the private jet industry and needs a re-designed website.

We have created the structure for the website and content inside of Tavoni.io (THESE ARE ONLY ROUGH A.I. GENERATED WIREFRAMES AND DO NOT NEED TO BE FOLLOWED EXACTLY) - https://www.tavoni.io/app/project/P482915_qRuVwKsLm-DDtaHrYuop72XNc8fkoPzqlrhwDxHkaWm3Tq

Take the content from the 'Home Page' under the 'Wireframe' tab on the Tavoni.io link above, but feel free to re-design the page in a better way as these are only A.I. generated wireframes.

We want a DARK theme.... High quality, luxurious feel, greyscale colors. Attached is a brand guideline (BUT THIS IS NOT A 100% BRAND GUIDELINE, YOU CAN CHANGE COLORS AND FONTS AND MAKE CHANGES IF YOU HAVE BETTER IDEAS) and attached is our logo. We are also attaching some examples of other apps and websites to give you a guideline of what we're looking for for this design project.

The final design MUST communicate luxury using high-quality imagery of large cabin luxurious private jets.

ENTRIES THAT DO NOT FOLLOW THE PROJECT BRIEF WILL BE AUTOMATICALLY DISCARDED. FOLLOW THE INSTRUCTIONS!

Industry/Entity Type

Travel

Number of Pages Required

1 page

Font styles to use
Sans Serif

Colors

Designer to choose colors to be used in the design.

Requirements
Must have
• Follow wireframe and use content in wireframe (see Tavoni.io link)

```html
<!DOCTYPE html>
<html lang="en">
<head>
<meta charset="utf-8">
<title>SoarVane — Luxury Private Jet Travel</title>
<link rel="stylesheet" href="https://fonts.googleapis.com/css2?family=Sarabun:wght@300;400;500&display=swap">
<style>
:root{
  --black:#141414;
  --ink:#222222;
  --dark:#2c2c2c;
  --mid:#575757;
  --grey:#6a6a6a;
  --line:#9a9a9a;
  --soft:#c9c9c9;
  --mist:#ececec;
  --white:#ffffff;
  --dusk:#b8743e;
}
*{box-sizing:border-box;margin:0;padding:0}
html,body{width:1200px;height:4231px;overflow:hidden}
body{font-family:"Sarabun",sans-serif;color:var(--white);background:var(--ink);font-weight:300}
.section{position:relative;width:1200px;overflow:hidden}
.abs{position:absolute}
.ph{position:absolute}
.btn{position:absolute;height:34px;display:flex;align-items:center;justify-content:center;font-size:11px;letter-spacing:.06em;text-transform:uppercase;font-weight:400}
.btn-solid{background:var(--white);color:var(--ink)}
.btn-line{border:1px solid var(--soft);color:var(--white)}
.btn-dark{background:var(--black);color:var(--white)}
.btn-line-dark{border:1px solid var(--ink);color:var(--ink)}
.eyebrow{font-size:10px;letter-spacing:.04em;display:flex;align-items:center;gap:8px;text-transform:uppercase}
.eyebrow::after{content:"";width:48px;height:1px;background:currentColor;opacity:.7}
.h2{font-size:30px;line-height:38px;font-weight:300;letter-spacing:.01em}
.body{font-size:11px;line-height:15px}

/* hero */
.hero{height:558px;background:linear-gradient(100deg,#1a1a1a 0%,#2e2e2e 40%,#3c3c3c 100%)}
.hero-photo{left:0;top:0;width:1200px;height:558px;
  background:
    radial-gradient(ellipse 360px 140px at 700px 470px,rgba(184,116,62,.55),rgba(184,116,62,0) 70%),
    radial-gradient(ellipse 420px 300px at 1000px 180px,rgba(200,200,200,.35),rgba(200,200,200,0) 70%),
    radial-gradient(ellipse 260px 420px at 1000px 300px,rgba(60,45,40,.8),rgba(60,45,40,0) 70%),
    linear-gradient(180deg,rgba(0,0,0,.15),rgba(0,0,0,.0) 40%,rgba(0,0,0,.45) 100%),
    linear-gradient(100deg,#1c1c1c 0%,#3a3a3a 45%,#6a6a6a 75%,#4a4a4a 100%)}
.nav{left:112px;top:15px;width:975px;height:31px;display:flex;align-items:center}
.logo{font-size:26px;font-weight:300;display:flex;align-items:center;gap:8px}
.logo i{width:16px;height:16px;background:var(--white);display:inline-block}
.menu{display:flex;gap:26px;margin-left:40px;font-size:11px;font-weight:400}
.menu span::after{content:" ⌄";font-size:10px}
.inquire{margin-left:auto;width:114px;height:31px;border:1px solid var(--soft);display:flex;align-items:center;justify-content:center;gap:8px;font-size:10px;letter-spacing:.06em}
.hero-title{left:112px;top:152px;font-size:44px;line-height:52px;font-weight:300}
.hero-text{left:112px;top:268px;width:460px}
.search-label{left:112px;top:428px;display:flex;align-items:center;gap:18px}
.search-label b{font-size:19px;font-weight:300}
.radio{font-size:10px;display:flex;align-items:center;gap:5px}
.radio i{width:9px;height:9px;border-radius:50%;border:1px solid var(--white);display:inline-block}
.radio i.on{background:var(--white)}
.field{position:absolute;top:464px;height:30px;border:1px solid var(--line);font-size:10px;display:flex;align-items:center;justify-content:space-between;padding:0 10px;color:var(--soft)}

/* features */
.features{height:227px;background:var(--white);color:var(--ink)}
.feature{position:absolute;top:54px;width:300px}
.feature .ic{width:59px;height:59px;border-radius:50%;background:var(--black);display:flex;align-items:center;justify-content:center}
.feature h3{margin-top:19px;font-size:16px;font-weight:400}
.feature p{margin-top:4px;font-size:11px;line-height:15px;color:#333}

/* fractional */
.fractional{height:530px;background:radial-gradient(ellipse 500px 300px at 900px 340px,#6a6a6a,#5b5b5b 70%)}
.photo-a{left:112px;top:52px;width:297px;height:335px;
  background:
    radial-gradient(ellipse 90px 170px at 95px 230px,#2a2d34,rgba(42,45,52,0) 80%),
    linear-gradient(180deg,#e4e6e8 0%,#c9ccd0 40%,#9c8b78 75%,#6d5f52 100%)}
.photo-b{left:286px;top:252px;width:241px;height:227px;
  background:
    radial-gradient(ellipse 120px 50px at 120px 110px,#f0f0f0,rgba(240,240,240,0) 80%),
    linear-gradient(180deg,#8a8a8a 0%,#bdbdbd 45%,#5a5a5a 75%,#2a2a2a 100%);
  border:2px solid var(--mid);outline:1px solid var(--soft);outline-offset:-1px}
.bullets{display:flex;gap:16px;font-size:11px}
.bullets span{display:flex;align-items:center;gap:6px}
.bullets span::before{content:"";width:10px;height:10px;border-radius:50%;background:var(--white)}

/* luxury */
.luxury{height:422px;background:var(--dark)}
.card{position:absolute;top:197px;width:315px;height:162px;border:1px solid var(--line);padding:28px 28px}
.card h3{margin-top:14px;font-size:14px;font-weight:400}
.card p{margin-top:6px;font-size:10px;line-height:14px;color:#aaa}

/* cta */
.cta{height:238px;background:linear-gradient(180deg,#ffffff 0%,#f3f3f3 55%,#d3d8dc 100%);color:var(--ink);text-align:center}
.center{left:0;width:1200px;text-align:center}

/* experience */
.experience{height:537px;background:linear-gradient(180deg,#6a6a6a,#626262)}
.exp-photo{left:834px;top:0;width:366px;height:537px;
  background:
    radial-gradient(ellipse 200px 120px at 120px 140px,rgba(255,255,255,.9),rgba(255,255,255,0) 75%),
    radial-gradient(ellipse 260px 140px at 260px 420px,rgba(250,250,252,.85),rgba(250,250,252,0) 75%),
    linear-gradient(175deg,#eef0f2 0%,#c5cad0 50%,#9aa0a6 100%)}
.exp-point{position:absolute;top:295px;width:210px}
.exp-point h4{font-size:14px;font-weight:400;display:flex;align-items:center;gap:8px}
.exp-point h4::before{content:"";width:10px;height:10px;border-radius:50%;background:var(--white)}
.exp-point p{margin:3px 0 0 18px;font-size:10px;line-height:13px}

/* faq */
.faq{height:727px;background:var(--dark)}
.faq-photo{left:112px;top:93px;width:410px;height:535px;border:2px solid var(--mid);
  background:
    radial-gradient(ellipse 130px 220px at 200px 300px,#7c7f86,rgba(124,127,134,0) 80%),
    linear-gradient(160deg,#e3ddd5 0%,#c6b9aa 40%,#8b7560 75%,#4a4440 100%)}
.faq-item{position:absolute;left:604px;width:483px;border:1px solid var(--soft);padding:0 18px;font-size:12px;display:flex;align-items:center;justify-content:space-between;height:41px}
.faq-open{display:block;height:106px;padding-top:12px}
.faq-open p{margin-top:10px;font-size:10px;line-height:14px;color:#ddd}

/* testimonial */
.testimonial{height:455px;background:linear-gradient(180deg,#ffffff,#f5f5f5 70%,#e3e5e7);color:var(--ink)}
.quote{left:112px;top:92px;width:490px;font-size:30px;line-height:38px;font-weight:300}
.stars{left:112px;top:312px;display:flex;gap:6px}
.person{left:112px;top:345px}
.person b{display:block;font-size:17px;font-weight:400}
.person span{display:block;margin-top:6px;font-size:9px}
.divider{left:254px;top:342px;width:1px;height:50px;background:#999}
.partner{left:284px;top:358px;display:flex;align-items:center;gap:6px;font-size:14px;font-weight:500}
.partner i{width:12px;height:12px;background:var(--ink);display:inline-block}
.testi-photo{left:673px;top:49px;width:414px;height:329px;
  background:
    radial-gradient(ellipse 110px 170px at 250px 200px,#3d3f44,rgba(61,63,68,0) 80%),
    radial-gradient(ellipse 120px 140px at 60px 90px,#2a2a2a,rgba(42,42,42,0) 80%),
    linear-gradient(170deg,#e8e2d6 0%,#c9bea9 50%,#8a857c 100%)}
.arrows{left:749px;top:345px;width:131px;height:59px;background:var(--dark);display:flex}
.arrows span{flex:1;display:flex;align-items:center;justify-content:center}
.arrows span+span{border-left:1px solid #555}

/* cta dark */
.cta-dark{height:257px;background:
  radial-gradient(ellipse 600px 160px at 600px 140px,rgba(90,90,90,.6),rgba(90,90,90,0) 75%),
  linear-gradient(180deg,#3a3a3a,#1e1e1e)}

/* footer */
.footer{height:280px;background:var(--ink)}
.col{position:absolute;top:38px}
.col h4{font-size:15px;font-weight:300}
.col ul{list-style:none;margin-top:8px}
.col li{font-size:9px;line-height:20px}
.social{left:112px;top:152px;display:flex;gap:11px}
.social i{width:22px;height:22px;border-radius:50%;border:1px solid var(--white);display:inline-block}
.news-input{left:770px;top:87px;width:213px;height:33px;border:1px solid var(--soft);font-size:10px;display:flex;align-items:center;padding-left:12px}
.news-btn{left:992px;top:87px;width:95px;height:33px;background:var(--white);color:var(--ink);font-size:10px;display:flex;align-items:center;justify-content:center;letter-spacing:.04em}
.rule{left:0;top:216px;width:1200px;height:1px;background:#555}
.legal{left:0;top:233px;width:1200px;display:flex;justify-content:center;gap:22px;font-size:8px;color:#bbb}
</style>
</head>
<body>

<!-- Hero -->
<section class="section hero">
  <div class="ph hero-photo" role="img" aria-label="Businessman walking beside a private jet on the tarmac at sunset"></div>
  <nav class="abs nav">
    <div class="logo">SoarVane<i></i></div>
    <div class="menu"><span>Aircraft</span><span>Programs</span><span>Why SoarVane</span><span>Lifestyle</span><span>Sustainability</span><span>Resources</span><span>Competitors</span></div>
    <div class="inquire">INQUIRE
      <svg width="12" height="12" viewBox="0 0 12 12"><path d="M1 6 11 1 8 11 6 7Z" fill="#fff"/></svg></div>
  </nav>
  <h1 class="abs hero-title">Experience the Ultimate<br>in Luxury Jet Travel</h1>
  <p class="abs body hero-text">SoarVane offers fractional jet ownership, jet card programs, private jet lease programs, all access programs, helicopter access programs, and by the seat charter flights. Discover the perfect flight program for your needs.</p>
  <div class="btn btn-solid" style="left:112px;top:336px;width:118px">Explore</div>
  <div class="btn btn-line" style="left:243px;top:336px;width:123px">Learn More</div>
  <div class="abs search-label"><b>Search Your Flight</b>
    <span class="radio"><i class="on"></i>Round Trip</span>
    <span class="radio"><i></i>One Way</span></div>
  <div class="field" style="left:112px;width:146px">Departure Airport <span>✈</span></div>
  <div class="field" style="left:271px;width:144px">Arrival Airport <span>✈</span></div>
  <div class="field" style="left:427px;width:144px">Departure Date <span>▦</span></div>
  <div class="field" style="left:591px;width:144px">Return Date <span>▦</span></div>
  <div class="field" style="left:755px;width:77px">Pax <span>⌄</span></div>
  <div class="btn btn-solid" style="left:850px;top:462px;width:81px">Search</div>
</section>

<!-- Program highlights -->
<section class="section features">
  <div class="feature" style="left:112px">
    <div class="ic"><svg width="28" height="28" viewBox="0 0 28 28" fill="none" stroke="#fff" stroke-width="1.5"><path d="M4 18h6l5 3 9-6-2-2-7 3M4 14h5l4 2"/><circle cx="17" cy="8" r="3"/></svg></div>
    <h3>Flexible Ownership Options Available</h3>
    <p>Choose from a variety of ownership programs and enjoy the freedom to fly on your own terms.</p>
  </div>
  <div class="feature" style="left:469px">
    <div class="ic"><svg width="28" height="28" viewBox="0 0 28 28" fill="none" stroke="#fff" stroke-width="1.5"><circle cx="14" cy="9" r="4"/><path d="M6 23c0-5 4-8 8-8s8 3 8 8"/><rect x="15" y="17" width="8" height="5"/></svg></div>
    <h3>Convenient Jet Card Programs</h3>
    <p>Access a fleet of private jets with our exclusive jet card programs, offering flexibility and convenience.</p>
  </div>
  <div class="feature" style="left:826px">
    <div class="ic"><svg width="28" height="28" viewBox="0 0 28 28" fill="none" stroke="#fff" stroke-width="1.5"><path d="M6 22 22 6M9 13l6 6M13 9l6 6"/><circle cx="8" cy="8" r="2"/><circle cx="20" cy="20" r="2"/></svg></div>
    <h3>Flexible Lease Programs</h3>
    <p>Experience the luxury of private jet travel without the commitment with our flexible lease programs.</p>
  </div>
</section>

<!-- Fractional ownership -->
<section class="section fractional">
  <div class="ph photo-a" role="img" aria-label="Man in a suit standing in front of a private jet"></div>
  <div class="ph photo-b" role="img" aria-label="Private jet parked on the runway, black and white"></div>
  <div class="abs eyebrow" style="left:589px;top:132px">Discover</div>
  <h2 class="abs h2" style="left:589px;top:155px">Experience the Luxury of<br>Fractional Jet Ownership</h2>
  <p class="abs body" style="left:589px;top:249px;width:430px">With SoarVane's fractional jet ownership program, you can enjoy the benefits of private jet travel without the hassle and expense of owning a whole aircraft. Our program offers flexibility, convenience, and access to a fleet of luxurious jets, allowing you to travel in style and comfort.</p>
  <div class="abs bullets" style="left:589px;top:329px"><span>Flexible Ownership Options</span><span>Convenient Booking Process</span><span>Luxurious Fleet of Jets</span></div>
  <div class="btn btn-solid" style="left:589px;top:367px;width:120px">Learn More</div>
  <div class="btn btn-line" style="left:722px;top:367px;width:115px">Sign Up</div>
</section>

<!-- Services -->
<section class="section luxury">
  <div class="abs eyebrow" style="left:112px;top:61px">Luxury</div>
  <h2 class="abs h2" style="left:112px;top:82px">Experience the Ultimate in<br>Private Jet Travel</h2>
  <p class="abs body" style="left:609px;top:69px;width:480px;font-size:10px;line-height:13px">SoarVane offers a wide range of exclusive services to meet your private jet travel needs. From fractional jet ownership to on-demand charter flights, we provide the highest level of luxury and convenience.</p>
  <div class="btn btn-solid" style="left:609px;top:118px;width:120px">Learn More</div>
  <div class="btn btn-line" style="left:742px;top:118px;width:113px">Sign Up</div>
  <div class="card" style="left:112px">
    <svg width="26" height="30" viewBox="0 0 26 30" fill="none" stroke="#fff" stroke-width="1.4"><circle cx="13" cy="10" r="8"/><circle cx="13" cy="10" r="4"/><path d="M8 17 6 28l7-4 7 4-2-11"/></svg>
    <h3>On-Demand Charter</h3><p>Fly anywhere, anytime with our on-demand<br>charter service.</p></div>
  <div class="card" style="left:443px">
    <svg width="30" height="30" viewBox="0 0 30 30" fill="none" stroke="#fff" stroke-width="1.4"><circle cx="15" cy="15" r="12"/><ellipse cx="15" cy="15" rx="5" ry="12"/><path d="M3 15h24M5 9h20M5 21h20"/></svg>
    <h3>Global Medical Response &amp; Recovery</h3><p>We provide specialized medical transportation<br>services worldwide.</p></div>
  <div class="card" style="left:772px">
    <svg width="32" height="30" viewBox="0 0 32 30" fill="none" stroke="#fff" stroke-width="1.4"><circle cx="23" cy="8" r="5"/><path d="M19 12 5 26l3 3M9 22l3 3M12 19l3 3"/></svg>
    <h3>Fractional Jet Ownership</h3><p>Enjoy the benefits of owning a private jet without<br>the hassles.</p></div>
</section>

<!-- Call to action -->
<section class="section cta">
  <h2 class="abs h2 center" style="top:65px">Experience luxury travel like never before</h2>
  <p class="abs center" style="top:105px;font-size:10px">Contact us today to book your exclusive jet experience</p>
  <div class="btn btn-dark" style="left:476px;top:138px;width:118px">Learn More</div>
  <div class="btn btn-line-dark" style="left:609px;top:138px;width:113px">Sign Up</div>
</section>

<!-- Experience -->
<section class="section experience">
  <div class="ph exp-photo" role="img" aria-label="Private jet flying above the clouds"></div>
  <div class="abs eyebrow" style="left:112px;top:111px">Experience</div>
  <h2 class="abs h2" style="left:112px;top:132px">Unparalleled Luxury and<br>Convenience for Private Aviation</h2>
  <p class="abs body" style="left:112px;top:226px;width:460px;font-size:10.5px">Discover the ultimate in luxury and convenience with SoarVane. Our exclusive private aviation solutions provide you with unparalleled access to the world of private jets, ensuring a seamless and extraordinary travel experience.</p>
  <div class="exp-point" style="left:112px"><h4>Convenience</h4><p>Enjoy hassle-free travel with our flexible scheduling and personalized services.</p></div>
  <div class="exp-point" style="left:364px"><h4>Luxury</h4><p>Indulge in the lavish amenities and exquisite interiors of our private jets.</p></div>
  <div class="btn btn-solid" style="left:112px;top:379px;width:119px">Learn More</div>
  <div class="btn btn-line" style="left:245px;top:379px;width:113px">Sign Up</div>
</section>

<!-- FAQ -->
<section class="section faq">
  <div class="ph faq-photo" role="img" aria-label="Woman on a phone call in a private jet cabin"></div>
  <h2 class="abs h2" style="left:604px;top:114px">Frequently</h2>
  <p class="abs" style="left:604px;top:158px;font-size:10px">Find answers to common questions about SoarVane's services and programs.</p>
  <div class="faq-item" style="top:190px">What is SoarVane? <span>+</span></div>
  <div class="faq-item faq-open" style="top:243px">How it works?
    <p>SoarVane works by allowing customers to purchase fractional ownership of a private jet, join jet card programs for a set number of flight hours, lease a private jet for a specific period, or access our all access and helicopter programs. We also offer charter flights where customers can book individual seats on private jets.</p></div>
  <div class="faq-item" style="top:362px">Why choose SoarVane? <span>+</span></div>
  <div class="faq-item" style="top:415px">How to book? <span>+</span></div>
  <div class="faq-item" style="top:468px">What are the benefits? <span>+</span></div>
  <p class="abs" style="left:604px;top:530px;font-size:12px">Still have questions?</p>
  <p class="abs" style="left:604px;top:550px;font-size:9px;color:#bbb">Contact us for more information.</p>
  <div class="btn btn-solid" style="left:604px;top:581px;width:118px">Learn More</div>
  <div class="btn btn-line" style="left:735px;top:581px;width:115px">Sign Up</div>
</section>

<!-- Testimonial -->
<section class="section testimonial">
  <blockquote class="abs quote">SoarVane's services have exceeded my expectations. The convenience and luxury of flying with them is unmatched.</blockquote>
  <div class="abs stars">
    <svg width="14" height="14" viewBox="0 0 14 14"><path d="M7 0l2 5h5l-4 3 2 6-5-4-5 4 2-6-4-3h5z" fill="#e0b800"/></svg>
    <svg width="14" height="14" viewBox="0 0 14 14"><path d="M7 0l2 5h5l-4 3 2 6-5-4-5 4 2-6-4-3h5z" fill="#e0b800"/></svg>
    <svg width="14" height="14" viewBox="0 0 14 14"><path d="M7 0l2 5h5l-4 3 2 6-5-4-5 4 2-6-4-3h5z" fill="#e0b800"/></svg>
    <svg width="14" height="14" viewBox="0 0 14 14"><path d="M7 0l2 5h5l-4 3 2 6-5-4-5 4 2-6-4-3h5z" fill="#e0b800"/></svg>
    <svg width="14" height="14" viewBox="0 0 14 14"><path d="M7 0l2 5h5l-4 3 2 6-5-4-5 4 2-6-4-3h5z" fill="#e0b800"/></svg>
  </div>
  <div class="abs person"><b>John Doe</b><span>CEO, Acme Corp</span></div>
  <div class="abs divider"></div>
  <div class="abs partner"><i></i>Lumora</div>
  <div class="ph testi-photo" role="img" aria-label="Man in a grey suit walking beside a private jet engine"></div>
  <div class="abs arrows">
    <span><svg width="24" height="10" viewBox="0 0 24 10" fill="none" stroke="#fff" stroke-width="1.3"><path d="M23 5H1M5 1 1 5l4 4"/></svg></span>
    <span><svg width="24" height="10" viewBox="0 0 24 10" fill="none" stroke="#fff" stroke-width="1.3"><path d="M1 5h22M19 1l4 4-4 4"/></svg></span>
  </div>
</section>

<!-- Closing call to action -->
<section class="section cta-dark">
  <h2 class="abs h2 center" style="top:56px">Experience luxury travel like never before</h2>
  <p class="abs center" style="top:97px"><span style="display:inline-block;width:680px;font-size:10px;line-height:13px">Discover the ultimate in private jet travel with SoarVane. Whether you're looking for fractional jet ownership, jet card programs, private jet lease programs, all access programs, helicopter access programs, or by the seat charter flights, we have the perfect solution for your travel needs.</span></p>
  <div class="btn btn-solid" style="left:476px;top:141px;width:118px">Book</div>
  <div class="btn btn-line" style="left:609px;top:141px;width:113px">Contact</div>
</section>

<!-- Footer -->
<footer class="section footer">
  <div class="abs logo" style="left:112px;top:60px">SoarVane<i></i></div>
  <p class="abs" style="left:112px;top:131px;font-size:9px;letter-spacing:.05em">FOLLOW US:</p>
  <div class="abs social"><i></i><i></i><i></i><i></i></div>
  <div class="col" style="left:356px"><h4>About Us</h4><ul><li>Charter</li><li>Fleet</li><li>Destinations</li><li>Pricing</li><li>Contact</li></ul></div>
  <div class="col" style="left:499px"><h4>Services</h4><ul><li>Private Jets</li><li>Helicopters</li><li>Jet Cards</li><li>Membership</li><li>FAQ</li></ul></div>
  <div class="col" style="left:642px"><h4>Terms</h4><ul><li>TERMS</li><li>Privacy</li><li>Careers</li><li>Press</li><li>Blog</li><li>Support</li></ul></div>
  <div class="col" style="left:770px"><h4>Subscribe to Our Newsletter</h4><ul><li>Join our mailing list for the latest updates.</li></ul></div>
  <div class="abs news-input">Enter Your Email</div>
  <div class="abs news-btn">SUBSCRIBE</div>
  <p class="abs" style="left:773px;top:130px;width:260px;font-size:8px;line-height:12px">By subscribing, you agree to our Privacy Policy and consent to receive updates.</p>
  <div class="abs rule"></div>
  <div class="abs legal"><span>© 2024 SoarVane. All rights reserved.</span><span>Privacy Policy</span><span>Terms of Service</span><span>Cookie Settings</span></div>
</footer>

</body>
</html>
```